The Ledgerline Business Card

Business card with QR Code for an accounting and tax business

Target Market(s)

Small Business and Individual Tax

Industry/Entity Type

Bookkeeping, Accounting and Taxes

Contact Information for Business Card

482 CALDWELL ST STE 2210 #614273 BOSTON, MA Zip: 02387

Requirements
Must have
• Name and Address

```html
<!DOCTYPE html>
<html lang="en">
<head>
<meta charset="utf-8">
<title>The Ledgerline – Business Card</title>
<link rel="stylesheet" href="https://fonts.googleapis.com/css2?family=Montserrat:wght@600;800&family=Lato:wght@400&display=swap">
<style>
  :root {
    --backdrop: #d8d8d8;
    --card: #ffffff;
    --brand-green: #137d6c;
    --ink: #474747;
    --ink-soft: #3d3d3d;
  }
  html, body {
    margin: 0;
    padding: 0;
    width: 1200px;
    height: 1000px;
    overflow: hidden;
    background: var(--backdrop);
  }
  .stage {
    width: 1200px;
    height: 1000px;
    display: flex;
    align-items: center;
    justify-content: center;
  }
  .business-card {
    position: relative;
    width: 840px;
    height: 500px;
    background: var(--card);
    border-radius: 46px;
    overflow: hidden;
    box-shadow: 0 2px 6px rgba(0,0,0,0.12);
  }
  .accent-bar {
    position: absolute;
    left: 262px;
    width: 26px;
    height: 72px;
    background: var(--brand-green);
  }
  .accent-bar--top { top: 0; }
  .accent-bar--bottom { bottom: 0; }

  .brand {
    position: absolute;
    left: 34px;
    top: 226px;
    width: 210px;
    display: flex;
    align-items: center;
    gap: 10px;
  }
  .brand-dot {
    flex: none;
    width: 16px;
    height: 16px;
    border-radius: 50%;
    background: var(--brand-green);
  }
  .brand-name {
    font-family: "Montserrat", sans-serif;
    font-weight: 600;
    font-size: 24px;
    line-height: 1.15;
    color: var(--brand-green);
  }

  .contact {
    position: absolute;
    left: 330px;
    top: 88px;
  }
  .contact-name {
    margin: 0;
    font-family: "Montserrat", sans-serif;
    font-weight: 800;
    font-size: 50px;
    letter-spacing: -0.5px;
    color: var(--ink);
    line-height: 1;
  }
  .contact-title {
    margin: 20px 0 0;
    font-family: "Lato", sans-serif;
    font-weight: 400;
    font-size: 24px;
    letter-spacing: 0.5px;
    color: var(--ink);
  }
  .contact-rule {
    width: 348px;
    height: 4px;
    margin: 18px 0 14px;
    background: var(--brand-green);
    border: 0;
  }
  .contact-address {
    margin: 0;
    font-family: "Lato", sans-serif;
    font-style: normal;
    font-size: 21px;
    line-height: 44px;
    color: var(--ink-soft);
  }
</style>
</head>
<body>
  <main class="stage">
    <article class="business-card">
      <div class="accent-bar accent-bar--top"></div>
      <div class="accent-bar accent-bar--bottom"></div>

      <div class="brand">
        <span class="brand-dot"></span>
        <span class="brand-name">The Ledgerline</span>
      </div>

      <section class="contact">
        <h1 class="contact-name">DANIEL REYES</h1>
        <p class="contact-title">BOOKKEEPER</p>
        <hr class="contact-rule">
        <address class="contact-address">
          482 CALDWELL ST<br>
          STE 2210<br>
          #614273 BOSTON,<br>
          MA Zip: 02387
        </address>
      </section>
    </article>
  </main>
</body>
</html>
```